MAGNET DESIGN

Magnet design for electrical company.(not a business card!)

The company services the domestic market

The magnet will be given to all customers..

Looking for a fun design and open minded to all ideas.

magnet size is 55mmx90mm with round edges

THIS IS A DESIGN FOR A FRIDGE MAGNET..... NOT A BUSINESS CARD...

Single sided.

Target Market(s)

Domestic market, home owners

Industry/Entity Type

Electrical

Requirements
Must have
• Picture of myself, without the car in the background
heading: your neighbourhood electrician
www.brightwirepros.example.com.au
1300 482 957

On time guaranteed
Up front pricing
No mess Guaranteed

( some of our services provided)
Switchboards/ safety switches/ celing fans/ power points/ phone & tv points/smoke alarms

Lic: 518264D (can be small in a corner)
ABN: 48259317604 (can be small in a corner)
Nice to have
• Logo

```html
<!DOCTYPE html>
<html lang="en">
<head>
<meta charset="utf-8">
<title>Your Neighbourhood Electrician – Fridge Magnet</title>
<link rel="stylesheet" href="https://fonts.googleapis.com/css2?family=Oswald:wght@600;700&family=Roboto+Condensed:wght@400;700&display=swap">
<style>
  :root {
    --page: #ffffff;
    --magnet-core: #ffd61f;
    --magnet-mid: #ffb41a;
    --magnet-edge: #f07c0e;
    --red: #e3231b;
    --orange: #e5631a;
    --white: #ffffff;
    --ink: #1a1a1a;
    --brown: #5a3a12;
    --shirt-blue: #2a52c9;
    --skin: #d9a47a;
  }
  * { margin: 0; padding: 0; box-sizing: border-box; }
  html, body {
    width: 733px; height: 1200px; overflow: hidden;
    background: var(--page);
  }
  .magnet {
    position: relative;
    width: 733px; height: 1200px;
    border-radius: 56px;
    overflow: hidden;
    background:
      repeating-linear-gradient(180deg, rgba(255,255,255,0.06) 0 3px, rgba(0,0,0,0) 3px 9px),
      radial-gradient(ellipse 60% 48% at 50% 50%, var(--magnet-core) 0%, var(--magnet-mid) 55%, var(--magnet-edge) 100%);
    font-family: "Oswald", "Arial Narrow", sans-serif;
  }
  .portrait {
    position: absolute;
    left: 196px; top: 40px;
    width: 352px; height: 500px;
    background:
      radial-gradient(ellipse 22% 18% at 50% 22%, var(--skin) 0 96%, rgba(0,0,0,0) 100%),
      radial-gradient(ellipse 50% 52% at 50% 72%, var(--shirt-blue) 0 80%, rgba(42,82,201,0) 100%);
    filter: blur(2px);
  }
  .headline { position: absolute; left: 0; top: 0; width: 100%; }
  .headline-your {
    position: absolute; left: 60px; top: 456px;
    font-size: 66px; font-weight: 700; line-height: 1;
    color: var(--red);
    letter-spacing: -1px;
    -webkit-text-stroke: 1.5px var(--white);
    text-shadow: 2px 3px 3px rgba(0,0,0,0.25);
  }
  .headline-neighbourhood {
    position: absolute; left: 100px; top: 524px;
    font-size: 86px; font-weight: 700; line-height: 1;
    color: var(--white);
    letter-spacing: -1px;
    text-shadow: 3px 4px 4px rgba(0,0,0,0.3);
  }
  .headline-electrician {
    position: absolute; left: 392px; top: 618px;
    font-size: 54px; font-weight: 700; line-height: 1;
    color: var(--orange);
    text-shadow: 2px 3px 3px rgba(0,0,0,0.28);
  }
  .services {
    position: absolute; left: 60px; top: 696px; width: 640px;
    font-family: Arial, Helvetica, sans-serif;
    font-size: 17.5px; line-height: 1.3;
    color: var(--ink);
  }
  .promises {
    position: absolute; left: 196px; top: 768px;
    list-style: none;
  }
  .promises li {
    font-size: 38px; font-weight: 600; line-height: 1;
    color: var(--white);
    margin-bottom: 33px;
    text-shadow: 0 14px 8px rgba(120,70,0,0.18), 2px 2px 3px rgba(0,0,0,0.2);
  }
  .contact-web {
    position: absolute; left: 190px; top: 988px;
    font-family: "Roboto Condensed", "Arial Narrow", sans-serif;
    font-size: 24px; color: var(--brown);
  }
  .contact-phone {
    position: absolute; left: 280px; top: 1034px;
    font-family: "Roboto Condensed", "Arial Narrow", sans-serif;
    font-size: 31px; font-weight: 700; color: var(--orange);
    text-shadow: 1px 2px 2px rgba(0,0,0,0.3);
  }
  .licence {
    position: absolute; left: 528px; top: 1104px;
    font-family: Arial, Helvetica, sans-serif;
    font-size: 16px; line-height: 1.4; color: var(--ink);
  }
</style>
</head>
<body>
  <main class="magnet">
    <div class="portrait" role="img" aria-label="Photo of the electrician smiling, wearing a blue and white work shirt"></div>

    <h1 class="headline">
      <span class="headline-your">YOUR</span>
      <span class="headline-neighbourhood">NEIGHBOURHOOD</span>
      <span class="headline-electrician">ELECTRICIAN</span>
    </h1>

    <p class="services">SwitchBoards | Safety Switches | Celing Fans | Power Points | Phone &amp; TV Points | Smoke Alarms</p>

    <ul class="promises">
      <li>ON TIME GUARANTEED</li>
      <li>UP FRONT PRICING</li>
      <li>NO MESS GUARANTEED</li>
    </ul>

    <p class="contact-web">Web : www.brightwirepros.example.com.au</p>
    <p class="contact-phone">1300 482 957</p>

    <p class="licence">Lic: 518264D<br>ABN: 48259317604</p>
  </main>
</body>
</html>
```